Zanquorra Business Card Design

Zanquorra is a small and new restaurant/ bar location in Hong Kong. The name "Djibouti" derives from an African country. There is no specific reason behind other than the fact, that the bar is somewhat inspired by African elements (only inspired but not purely based on African cuisine etc.).

The bar is somewhat a fusion of African, Mediterranean and Oriental (Old French Vietnam) elements.

However, it is very imperative to stress, that the overall look and feel of Zanquorra is a very high end cocktail lounge/ bar location. The bar is tucked away in a hidden alley, so people will have to know about it. The idea is to send the consumer off in an Escape or hidden remote location where they are at ease in a hip, stylish and trendy environment.

The card needs to feel high-end.

Final logo artwork has been attached and also pictures of the bar/ restaurant itself. The logo ie monkey head cannot be modified. However, the background color and the color of the type "ZANQUORRA" can be changed.

The following details need to fit onto the business card. Of course they can be arranged to your liking:

LOGO

Colin Vey
Partner

+852 97035164
xxx@zanquorra.com
www.zanquorra.com
7C, Brennick Road, Wan Chai, Hong Kong

```html
<!DOCTYPE html>
<html lang="en">
<head>
<meta charset="utf-8">
<title>Zanquorra Business Card</title>
<link rel="stylesheet" href="https://fonts.googleapis.com/css2?family=Almendra:wght@400;700&display=swap">
<style>
  :root {
    --page: #ececec;
    --paper: #ffffff;
    --wine-dark: #3a0306;
    --wine: #7a0a10;
    --wine-bright: #a8141b;
    --ink: #2b1a12;
    --mark: #3b2418;
    --light-text: #ffffff;
  }
  * { box-sizing: border-box; margin: 0; padding: 0; }
  html, body { width: 1200px; height: 977px; overflow: hidden; }
  body {
    background: var(--page);
    font-family: "Almendra", Georgia, serif;
    position: relative;
  }
  .card {
    position: absolute;
    width: 600px;
    height: 343px;
    border-radius: 3px;
    overflow: hidden;
    box-shadow: 0 10px 24px rgba(0,0,0,0.18);
    background: var(--paper);
  }
  .card-front { left: 60px; top: 70px; }
  .card-back { left: 540px; top: 560px; }

  .bar-photo {
    position: absolute;
    inset: 0;
    background:
      radial-gradient(ellipse at 70% 25%, var(--wine-bright) 0%, transparent 55%),
      radial-gradient(ellipse at 20% 75%, var(--wine) 0%, transparent 60%),
      linear-gradient(135deg, var(--wine) 0%, var(--wine-dark) 100%);
  }

  .brand {
    position: absolute;
    display: flex;
    flex-direction: column;
    align-items: center;
  }
  .brand-disc {
    border-radius: 50%;
    background: var(--mark);
  }
  .brand-name {
    font-weight: 700;
    letter-spacing: 2px;
    line-height: 1;
  }

  .card-front .brand { left: 0; right: 0; top: 62px; }
  .card-front .brand-disc {
    width: 150px; height: 150px;
    border: 5px solid var(--paper);
  }
  .card-front .brand-name {
    color: var(--light-text);
    font-size: 46px;
    margin-top: 32px;
  }

  .back-panel {
    position: absolute;
    left: 0; top: 0; bottom: 0;
    width: 262px;
    background: var(--paper);
  }
  .card-back .bar-photo { left: 262px; }
  .card-back .brand { left: 0; width: 262px; top: 78px; }
  .card-back .brand-disc { width: 118px; height: 118px; }
  .card-back .brand-name {
    color: var(--ink);
    font-size: 32px;
    margin-top: 22px;
  }

  .details {
    position: absolute;
    left: 300px;
    top: 40px;
    color: var(--light-text);
  }
  .person-name, .person-role {
    font-size: 21px;
    font-weight: 700;
    line-height: 1.2;
  }
  .contact-list {
    list-style: none;
    margin-top: 22px;
  }
  .contact-list li {
    display: flex;
    align-items: flex-start;
    gap: 12px;
    font-size: 17px;
    line-height: 1.25;
    margin-bottom: 9px;
  }
  .contact-icon {
    flex: 0 0 20px;
    width: 20px; height: 20px;
    margin-top: 1px;
  }
</style>
</head>
<body>

  <section class="card card-front">
    <div class="bar-photo" role="img" aria-label="Red-toned photograph of the bar interior with lanterns and seating"></div>
    <div class="brand">
      <div class="brand-disc"></div>
      <div class="brand-name">ZANQUORRA</div>
    </div>
  </section>

  <section class="card card-back">
    <div class="back-panel">
      <div class="brand">
        <div class="brand-disc"></div>
        <div class="brand-name">ZANQUORRA</div>
      </div>
    </div>
    <div class="bar-photo" role="img" aria-label="Red-toned photograph of the bar entrance with a glowing sign"></div>
    <div class="details">
      <p class="person-name">Colin Vey</p>
      <p class="person-role">Partner</p>
      <ul class="contact-list">
        <li>
          <svg class="contact-icon" viewBox="0 0 20 20" aria-hidden="true">
            <circle cx="10" cy="10" r="10" fill="#fff"/>
            <rect x="7" y="4.5" width="6" height="11" rx="1.2" fill="none" stroke="#7a0a10" stroke-width="1.4"/>
          </svg>
          <span>+852 97035164</span>
        </li>
        <li>
          <svg class="contact-icon" viewBox="0 0 20 20" aria-hidden="true">
            <circle cx="10" cy="10" r="10" fill="#fff"/>
            <rect x="5" y="6.5" width="10" height="7" fill="none" stroke="#7a0a10" stroke-width="1.4"/>
            <path d="M5 6.5 L10 10.5 L15 6.5" fill="none" stroke="#7a0a10" stroke-width="1.4"/>
          </svg>
          <span>xxx@zanquorra.com</span>
        </li>
        <li>
          <svg class="contact-icon" viewBox="0 0 20 20" aria-hidden="true">
            <circle cx="10" cy="10" r="10" fill="#fff"/>
            <circle cx="10" cy="10" r="5.5" fill="none" stroke="#7a0a10" stroke-width="1.3"/>
            <ellipse cx="10" cy="10" rx="2.4" ry="5.5" fill="none" stroke="#7a0a10" stroke-width="1.1"/>
            <line x1="4.5" y1="10" x2="15.5" y2="10" stroke="#7a0a10" stroke-width="1.1"/>
          </svg>
          <span>www.zanquorra.com</span>
        </li>
        <li>
          <svg class="contact-icon" viewBox="0 0 20 20" aria-hidden="true">
            <circle cx="10" cy="10" r="10" fill="#fff"/>
            <path d="M10 15.5 C7 11.5 6 10 6 8.2 A4 4 0 0 1 14 8.2 C14 10 13 11.5 10 15.5 Z" fill="#7a0a10"/>
            <circle cx="10" cy="8.2" r="1.5" fill="#fff"/>
          </svg>
          <span>7C, Brennick Road,<br>Wan Chai, Hong Kong</span>
        </li>
      </ul>
    </div>
  </section>

</body>
</html>
```